Real Estate investor needs stationary design.

We need business cards, letterhead, and envelope design using our new logo. The customer we are marketing to is someone who is in desperate need to sell or get rid of their home. These people are going to be stressed and under pressure. Need to convey something soothing and credible.

The logo color is Blue Hex Color: #0088CE; RGB: (0,136,206)
This looks great with Black Hex Code: #D3A205; RGB: (0,0,0)
This looks great with Silver #A5ACAF; RGB: (165,172,175)

The back of the business card should have my logo and tagline as a light background so I can add notes or information later.

I'm thinking the front should have the silver color given above as the background, with my logo (logo files will be uploaded on Monday October 12th as I am awaiting my logo files from PixelHarbor, they are being reviewed). Maybe the background could have a texture like wood, or drywall, or siding, or stucco, a house, something having to do with houses.

Please make sure to provide a business card, envelope, and letterhead design as that is the package I chose. Thank you!
Updates

I have uploaded the completed logo and just the owl files. They were just approved. Thank you. They are in .ai, .eps, .jpg, .pdf, .png. Added Monday, October 12, 2015

Target Market(s)

home owners

Industry/Entity Type

Real Estate

Requirements
Must have
• Must have my new logo. The font is Trajan Pro.

```html
<!DOCTYPE html>
<html lang="en">
<head>
<meta charset="utf-8">
<title>Tovanwick Estates Letterhead</title>
<link href="https://fonts.googleapis.com/css2?family=Montserrat:wght@400;600;700&display=swap" rel="stylesheet">
<style>
  :root {
    --brand-blue: #0088ce;
    --text-blue: #3a8fd0;
    --paper: #ffffff;
  }
  html, body {
    margin: 0;
    padding: 0;
    width: 816px;
    height: 1200px;
    overflow: hidden;
    background: var(--paper);
  }
  .letterhead {
    position: relative;
    width: 816px;
    height: 1200px;
    background: var(--paper);
    font-family: "Montserrat", sans-serif;
  }
  .brand-mark {
    position: absolute;
    left: 74px;
    top: 50px;
    width: 60px;
    height: 60px;
    border-radius: 50%;
    background: var(--brand-blue);
  }
  .brand-name {
    position: absolute;
    right: 24px;
    top: 66px;
    width: 200px;
    text-align: center;
    color: var(--brand-blue);
    font-weight: 600;
    line-height: 1;
  }
  .brand-name .primary {
    display: block;
    font-size: 25px;
    letter-spacing: 1.5px;
  }
  .brand-name .secondary {
    display: block;
    margin-top: 8px;
    font-size: 12px;
    letter-spacing: 5px;
  }
  .header-rule {
    position: absolute;
    left: 34px;
    right: 24px;
    top: 127px;
    height: 2px;
    background: var(--brand-blue);
  }
  .contact-block {
    position: absolute;
    right: 14px;
    top: 141px;
    text-align: right;
    font-style: normal;
    color: var(--text-blue);
  }
  .contact-block .department {
    font-size: 15px;
    font-weight: 700;
    color: var(--brand-blue);
    margin-bottom: 10px;
  }
  .contact-block .line {
    font-size: 14.5px;
    font-weight: 400;
    line-height: 18.5px;
  }
</style>
</head>
<body>
  <main class="letterhead">
    <div class="brand-mark"></div>
    <div class="brand-name">
      <span class="primary">TOVANWICK</span>
      <span class="secondary">ESTATES</span>
    </div>
    <div class="header-rule"></div>
    <address class="contact-block">
      <div class="department">DEPARTMENT</div>
      <div class="line">### Roadname</div>
      <div class="line">City, Zipcode ###</div>
      <div class="line">PHONE: ######</div>
      <div class="line">Fax: ######</div>
      <div class="line">website.com</div>
    </address>
  </main>
</body>
</html>
```